Roofing company in Toronto, Canada needs a logo design and business card design

We need a business card and logo created for our company. Our company is "KVL Roofing" which provides roofing services for commercial and residential customers. We serve customers in the Greater Toronto Area (in Canada) thus the name KVL.

We want the logo and business card to be a modern design displaying professionalism and quality in the work. We would prefer rounded corners for the business cards but are open to other ideas. The cards should be pleasant and appealing to customers.

Target Market(s)

Commercial and Residential customers

Industry/Entity Type

Roofing

Contact Information for Business Card

Logo Text

KVL Roofing

Requirements
Nice to have
• Colours that are pleasing to the eye but at the same time should stand out from other business cards. If the design can incorporate the name of KVL Roofing and the actual concept of roofing that would be nice.
Should not have
• Do not want the business cards or logo to be childish looking. Need to look professionally designed.

```html
<!DOCTYPE html>
<html lang="en">
<head>
<meta charset="UTF-8">
<title>KVL Roofing – Business Card</title>
<link href="https://fonts.googleapis.com/css2?family=Lato:wght@400;700;900&family=Michroma&display=swap" rel="stylesheet">
<style>
  :root {
    --backdrop: #757575;
    --card-light: #f9f9f9;
    --card-dark: #0b0b0e;
    --brand-red: #b3121b;
    --name-red: #8c1016;
    --text-grey: #444444;
    --title-grey: #555555;
    --logo-light: #e6e6e6;
  }
  html, body {
    margin: 0;
    padding: 0;
    width: 1200px;
    height: 900px;
    overflow: hidden;
    background: var(--backdrop);
  }
  .canvas {
    position: relative;
    width: 1200px;
    height: 900px;
  }
  .card {
    position: absolute;
    top: 192px;
    height: 491px;
    border-radius: 14px;
    box-shadow: 0 2px 6px rgba(0,0,0,0.25);
    box-sizing: border-box;
    overflow: hidden;
  }
  .card-front {
    left: 295px;
    width: 301px;
    background: var(--card-light);
    text-align: center;
  }
  .card-back {
    left: 621px;
    width: 305px;
    background: radial-gradient(ellipse at 50% 45%, #1c1c20 0%, var(--card-dark) 75%);
  }
  .wordmark {
    position: absolute;
    left: 30px;
    right: 30px;
    font-family: 'Lato', sans-serif;
    font-weight: 900;
    font-size: 27px;
    line-height: 1;
    text-transform: uppercase;
    letter-spacing: 1.5px;
    white-space: nowrap;
    display: flex;
    align-items: center;
    justify-content: center;
    gap: 8px;
  }
  .wordmark-mark {
    flex: 0 0 auto;
    width: 12px;
    height: 12px;
  }
  .card-front .wordmark {
    top: 88px;
    color: var(--brand-red);
  }
  .card-front .wordmark-mark { background: var(--brand-red); }
  .card-back .wordmark {
    top: 232px;
    color: var(--logo-light);
  }
  .card-back .wordmark-mark { background: var(--logo-light); }
  .person {
    position: absolute;
    top: 234px;
    left: 0;
    right: 0;
  }
  .person-name {
    font-family: 'Michroma', sans-serif;
    font-size: 18px;
    color: var(--name-red);
    letter-spacing: 1px;
    line-height: 24px;
    margin: 0;
  }
  .person-title {
    font-family: 'Lato', sans-serif;
    font-size: 16px;
    color: var(--title-grey);
    line-height: 20px;
    margin: 0;
    letter-spacing: 0.5px;
  }
  .divider {
    position: absolute;
    left: 55px;
    width: 190px;
    height: 1px;
    background: linear-gradient(to right, rgba(179,18,27,0), var(--brand-red) 50%, rgba(179,18,27,0));
  }
  .divider-top { top: 290px; }
  .divider-bottom { top: 378px; }
  .contact, .address {
    position: absolute;
    left: 0;
    right: 0;
    margin: 0;
    font-family: 'Lato', sans-serif;
    font-size: 16px;
    line-height: 23.5px;
    color: var(--text-grey);
    font-style: normal;
  }
  .contact { top: 299px; }
  .address { top: 388px; line-height: 20px; }
  .contact span, .address span { display: block; }
</style>
</head>
<body>
<main class="canvas">
  <section class="card card-front" aria-label="Business card front">
    <div class="wordmark"><span>KVL Roofing</span><span class="wordmark-mark"></span></div>
    <div class="person">
      <p class="person-name">DANIEL REYES</p>
      <p class="person-title">PRESIDENT</p>
    </div>
    <div class="divider divider-top"></div>
    <p class="contact">
      <span>416.555.0182</span>
      <span>hello@kvlroofing.ca</span>
      <span>www.kvlroofing.ca</span>
    </p>
    <div class="divider divider-bottom"></div>
    <address class="address">
      <span>240 Birchmount Road</span>
      <span>Toronto, ON M1N 3J8</span>
    </address>
  </section>
  <section class="card card-back" aria-label="Business card back">
    <div class="wordmark"><span>KVL Roofing</span><span class="wordmark-mark"></span></div>
  </section>
</main>
</body>
</html>
```